Business Card Design Project

Hi Designers, this project is currently on hold until the Logo is completed:
Please submit to the Logo project here:
http://work.pitchvault.example/brief.aspx?id=413907

Once logo is completed, it will be attached to this project for you to create business cards with show logo, company name and address

Maren T R Quillby

Osric's Tiny Grey Heron Co.
Fernbrook
Nether Coombsby
North Devon EX91 4TZ

Tel: 01809 417356
Mobile: 07900 263818
email: maren@tiny-grey-heron.example.co.uk

Project Deadline Extended
Reason: Sorry everyone, we have had a sick ewe and I am now behind with this one and need to extend the deadline. Best wishes Maren

The designer who wins the logo brief will be asked to design the business card. Many thanks Maren

Project Deadline Extended
Reason: Sorry everyone, just a chaotic time of year with animals. Need to extend the deadline again..... as I just haven't had enough time to take a good look.... Thank you for your understanding. Maren

Project Deadline Extended
Reason: Sorry everyone It is our busiest time of year with animals and just no time to spend going through such great designs. I will have to extend the deadline again and hopefully have some news very soon. Wishing you all a very happy Christmas and a happy and healthy new year. Maren & Osric

High end market
Boutique restaurants for meat (it's not commercial lamb it's a slow matured quality meat more like venison/beef) expensive - specialized market

High End shoot clothing / wool / sheepskin rugs
Quality products

Business

• based on the logo - (which Pitch Vault has just been asked to do)
possibly based on a simplified picture of a Hebridean Ram (shows it's a Hebridean by it's horns as opposed to other black sheep!!)

```html
<!DOCTYPE html>
<html lang="en">
<head>
<meta charset="utf-8">
<title>Osric's Tiny Grey Heron Co. – Business Card</title>
<link rel="stylesheet" href="https://fonts.googleapis.com/css2?family=Source+Sans+3:wght@400&display=swap">
<style>
  :root {
    --backdrop: #3b3b3b;
    --card-frame: #262a29;
    --panel: #ecedeb;
    --ink: #2b302f;
    --ink-light: #f1f1ef;
    --ring-edge: #d9dbd8;
  }
  * { box-sizing: border-box; margin: 0; padding: 0; }
  html, body {
    width: 1200px;
    height: 750px;
    overflow: hidden;
    background: var(--backdrop);
    font-family: "Source Sans 3", "Myriad Pro", Arial, sans-serif;
  }
  .card {
    position: absolute;
    left: 47px;
    top: 34px;
    width: 1106px;
    height: 682px;
    background: var(--card-frame);
  }
  .card-face {
    position: absolute;
    left: 52px;
    top: 56px;
    width: 1001px;
    height: 567px;
    background: var(--panel);
    overflow: hidden;
  }
  .brand {
    position: absolute;
    left: 39px;
    top: 11px;
    height: 139px;
    display: flex;
    align-items: center;
    gap: 20px;
  }
  .brand-dot {
    width: 139px;
    height: 139px;
    border-radius: 50%;
    background: var(--ink);
    flex: none;
  }
  .brand-name {
    color: var(--ink);
    font-size: 26px;
    font-weight: 400;
    white-space: nowrap;
  }
  .holder-name {
    position: absolute;
    right: 32px;
    top: 30px;
    color: var(--ink);
    font-size: 46px;
    font-weight: 400;
    white-space: nowrap;
  }
  .address-band {
    position: absolute;
    left: 0;
    top: 231px;
    width: 633px;
    height: 189px;
    background: var(--ink);
    color: var(--ink-light);
    padding: 10px 0 0 39px;
    font-size: 30px;
    font-style: normal;
    line-height: 43px;
  }
  .contact {
    position: absolute;
    left: 35px;
    top: 432px;
    color: var(--ink);
    font-size: 30px;
    line-height: 43px;
    white-space: nowrap;
  }
  .emblem {
    position: absolute;
    left: 600px;
    top: 143px;
    width: 400px;
    height: 400px;
  }
</style>
</head>
<body>
  <div class="card">
    <div class="card-face">
      <div class="brand">
        <div class="brand-dot"></div>
        <div class="brand-name">Osric's Tiny Grey Heron Co.</div>
      </div>

      <h1 class="holder-name">Maren T R Quillby</h1>

      <address class="address-band">
        Osric's Tiny Grey Heron Co.<br>
        Fernbrook<br>
        Nether Coombsby<br>
        North Devon EX91 4TZ
      </address>

      <div class="contact">
        Tel: 01809 417356<br>
        Mobile: 07900 263818<br>
        email: maren@tiny-grey-heron.example.co.uk
      </div>

      <svg class="emblem" viewBox="0 0 400 400" role="img" aria-label="Large brand emblem area">
        <circle cx="200" cy="200" r="197" fill="var(--ink)" stroke="var(--ring-edge)" stroke-width="4"/>
      </svg>
    </div>
  </div>
</body>
</html>
```